Redesign of an insurance website

Attached is an insurance website that I need to redesign. Currently the website is too dark. I like for example www.brambleshield.com . Could you make the website lighter and change the structure a little so that it is more user friendly?

Industry/Entity Type

Insurance

Number of Pages Required

4 page

```html
<!DOCTYPE html>
<html lang="cs">
<head>
<meta charset="utf-8">
<title>Jistotka.cz</title>
<link href="https://fonts.googleapis.com/css2?family=Jost:wght@400;500;600&display=swap" rel="stylesheet">
<style>
:root{
  --blue:#2f7cf0;
  --blue-light:#5fa0f5;
  --orange:#ff7a1a;
  --orange-soft:#ff9c4a;
  --orange-dark:#f5782a;
  --ink:#1c1c1c;
  --text:#3a3a3a;
  --footer:#2e2e2e;
  --white:#ffffff;
}
*{box-sizing:border-box;margin:0;padding:0}
html,body{width:837px;height:1200px;overflow:hidden;background:var(--white)}
body{position:relative;font-family:"Jost",sans-serif;color:var(--text)}
.abs{position:absolute}
.header{left:0;top:0;width:837px;height:35px;background:var(--white)}
.btn-small{position:absolute;top:10px;height:14px;color:var(--white);font-size:9px;line-height:14px;padding-left:3px;display:flex;align-items:center}
.btn-small .arr{position:absolute;right:0;top:0;width:13px;height:14px;display:flex;align-items:center;justify-content:center}
.btn-blue{background:var(--blue-light)}.btn-blue .arr{background:var(--blue)}
.btn-orange{background:var(--orange-soft)}.btn-orange .arr{background:var(--orange)}
.brand{font-weight:600;letter-spacing:1px}
.logo{left:0;width:837px;top:5px;text-align:center;font-size:19px;color:var(--blue)}
.nav{top:14px;font-size:10px;color:var(--ink);display:flex;gap:11px;left:582px}
.nav .active{color:var(--blue);border-bottom:1px solid var(--blue)}
.hero{left:0;top:35px;width:837px;height:394px;background:linear-gradient(180deg,#c9d8e6 0%,#e3e7ea 40%,#d9cdb8 70%,#e8dccb 100%)}
.picker{left:173px;top:259px;width:491px;height:170px;background:rgba(255,255,255,.78);border-radius:16px 16px 0 0}
.picker h2{position:absolute;top:13px;width:100%;text-align:center;font-weight:400;font-size:17px;color:var(--ink)}
.opt{position:absolute;top:54px;width:80px;text-align:center;font-size:8px;line-height:12px;color:var(--ink)}
.opt .circle{width:62px;height:62px;border-radius:50%;border:1.5px solid var(--blue);margin:0 auto 20px;display:flex;align-items:center;justify-content:center}
.opt.on .circle{background:var(--orange);border-color:var(--orange)}
.opt.on{color:var(--orange)}
.chev{position:absolute;top:78px}
.h-section{color:var(--blue);font-weight:400;font-size:18px}
.rule{height:1.5px;width:75px;background:var(--orange)}
.benefits{left:98px;top:522px;list-style:none}
.benefits li{height:24.7px;font-size:12px;display:flex;align-items:center;gap:7px;color:var(--ink)}
.form{left:504px;top:478px;width:234px;height:219px;background:var(--orange-soft);box-shadow:0 4px 5px rgba(0,0,0,.15)}
.form-head{height:30px;background:var(--orange-dark);color:var(--white);font-size:12px;line-height:30px;padding-left:12px}
.field{position:absolute;left:19px;width:196px;height:25px;border:1px solid #ffd4b0;border-radius:2px;color:#ffe9d8;font-size:9px;line-height:23px;padding-left:7px}
.consent{position:absolute;left:19px;top:159px;font-size:8.5px;color:var(--white);display:flex;gap:5px;align-items:center}
.form .btn-small{top:186px;left:18px;width:93px;font-size:9.5px;height:17px;line-height:17px}
.form .btn-small .arr{height:17px;width:17px}
.form .brand{position:absolute;left:128px;top:186px;color:var(--white);font-size:10px;line-height:17px}
.photo{left:97px;top:795px;width:275px;height:228px;border:2px solid #c9cdd2;background:linear-gradient(160deg,#5c6b78,#3d4a55)}
.para{font-size:9.5px;line-height:15.7px;color:var(--text);text-align:justify}
.newsletter{left:0;top:1077px;width:837px;height:86px;background:var(--blue-light)}
.newsletter .label{position:absolute;left:99px;top:33px;color:var(--white);font-size:15px}
.newsletter .input{position:absolute;left:283px;top:22px;width:354px;height:42px;background:#dbe9ff;border-radius:4px 0 0 4px;color:#9bb4da;font-style:italic;font-size:13px;line-height:42px;padding-left:17px}
.newsletter .submit{position:absolute;left:637px;top:22px;width:101px;height:42px;background:var(--orange);color:var(--white);font-size:15px;line-height:42px;text-align:center;border-radius:0 3px 3px 0}
.footer{left:0;top:1163px;width:837px;height:37px;background:var(--footer)}
.footer .brand{position:absolute;left:100px;top:11px;color:#d9d9d9;font-size:12px}
.social{position:absolute;top:9px;width:19px;height:19px;background:var(--orange)}
.legal{position:absolute;right:99px;top:5px;text-align:right;font-size:7.5px;line-height:14px;color:#cfcfcf}
</style>
</head>
<body>
<header class="abs header">
  <div class="btn-small btn-blue" style="left:98px;width:75px">PRIHLASIT SE<span class="arr"><svg width="9" height="6"><path d="M0 3h8M5 0l3 3-3 3" stroke="#fff" fill="none"/></svg></span></div>
  <div class="btn-small btn-orange" style="left:179px;width:76px">REGISTROVAT<span class="arr"><svg width="9" height="6"><path d="M0 3h8M5 0l3 3-3 3" stroke="#fff" fill="none"/></svg></span></div>
  <div class="abs logo brand">JISTOTKA.CZ</div>
  <nav class="abs nav"><span class="active">O NAS</span><span>CASTE DOTAZY</span><span>KONTAKT</span></nav>
</header>

<section class="abs hero" role="img" aria-label="Fotografie: dvojice odpočívá v lehátkách pod slunečníkem na pláži u moře"></section>

<section class="abs picker">
  <h2>CHCETE POJISTIT NECO JINEHO ?</h2>
  <svg class="chev" style="left:33px" width="10" height="16"><path d="M8 1L2 8l6 7" stroke="#666" stroke-width="1.5" fill="none"/></svg>
  <svg class="chev" style="left:441px" width="10" height="16"><path d="M2 1l6 7-6 7" stroke="#666" stroke-width="1.5" fill="none"/></svg>
  <div class="opt on" style="left:51px"><div class="circle"><svg width="36" height="24"><rect x="2" y="9" width="16" height="9" rx="3" fill="#fff"/><rect x="16" y="11" width="17" height="9" rx="3" fill="#fff"/><circle cx="7" cy="19" r="2" fill="#fff"/><circle cx="28" cy="21" r="2" fill="#fff"/><path d="M18 2v5M15 4l2 3M21 4l-2 3" stroke="#fff"/></svg></div>Lorem Ipsum<br>aorsum</div>
  <div class="opt" style="left:153px"><div class="circle"><svg width="30" height="30"><path d="M15 3l3 9 9 4v3l-9-2-1 6 3 3v2l-5-2-5 2v-2l3-3-1-6-9 2v-3l9-4z" fill="#2f7cf0" transform="rotate(45 15 15)"/></svg></div>Lorem Ipsum<br>aorsum</div>
  <div class="opt" style="left:256px"><div class="circle"><svg width="28" height="24"><path d="M14 2L2 12h4v10h16V12h4z" fill="#2f7cf0"/><rect x="11" y="15" width="6" height="7" fill="#fff"/></svg></div>Lorem Ipsum<br>aorsum</div>
  <div class="opt" style="left:359px"><div class="circle"><svg width="32" height="16"><path d="M2 9l3-5h18l6 5v4H2z" fill="#2f7cf0"/><circle cx="8" cy="13" r="2.5" fill="#fff" stroke="#2f7cf0"/><circle cx="24" cy="13" r="2.5" fill="#fff" stroke="#2f7cf0"/></svg></div>Lorem Ipsum<br>aorsum</div>
</section>

<h2 class="abs h-section" style="left:98px;top:488px">PROC HLEDAT POJISTENI PRES JISTOTKA.CZ?</h2>
<div class="abs rule" style="left:98px;top:513px"></div>
<ul class="abs benefits">
  <li><svg width="11" height="11"><rect x=".5" y="1.5" width="9" height="9" fill="none" stroke="#2f7cf0"/><path d="M2 5l3 3 6-7" stroke="#2f7cf0" stroke-width="1.8" fill="none"/></svg>s námi najdete tu nejvýhodnější nabídku</li>
  <li><svg width="11" height="11"><rect x=".5" y="1.5" width="9" height="9" fill="none" stroke="#2f7cf0"/><path d="M2 5l3 3 6-7" stroke="#2f7cf0" stroke-width="1.8" fill="none"/></svg>zaručíme vám nejlepší cenu na trhu</li>
  <li><svg width="11" height="11"><rect x=".5" y="1.5" width="9" height="9" fill="none" stroke="#2f7cf0"/><path d="M2 5l3 3 6-7" stroke="#2f7cf0" stroke-width="1.8" fill="none"/></svg>stačí pár minut a můžete ušetřit tisíce</li>
  <li><svg width="11" height="11"><rect x=".5" y="1.5" width="9" height="9" fill="none" stroke="#2f7cf0"/><path d="M2 5l3 3 6-7" stroke="#2f7cf0" stroke-width="1.8" fill="none"/></svg>srovnáváme všechny pojišťovny</li>
  <li><svg width="11" height="11"><rect x=".5" y="1.5" width="9" height="9" fill="none" stroke="#2f7cf0"/><path d="M2 5l3 3 6-7" stroke="#2f7cf0" stroke-width="1.8" fill="none"/></svg>zařídíme vám všechny druhy pojištění</li>
  <li><svg width="11" height="11"><rect x=".5" y="1.5" width="9" height="9" fill="none" stroke="#2f7cf0"/><path d="M2 5l3 3 6-7" stroke="#2f7cf0" stroke-width="1.8" fill="none"/></svg>vše vyřídíte z pohodlí domova</li>
  <li><svg width="11" height="11"><rect x=".5" y="1.5" width="9" height="9" fill="none" stroke="#2f7cf0"/><path d="M2 5l3 3 6-7" stroke="#2f7cf0" stroke-width="1.8" fill="none"/></svg>nemusíte nikam chodit a ušetříte</li>
</ul>

<form class="abs form">
  <div class="form-head">NAJDETE NEJVYHODNEJSI POJISTENI</div>
  <div class="field" style="top:44px">Jmeno</div>
  <div class="field" style="top:83px">Prijmeni</div>
  <div class="field" style="top:122px">E-mail</div>
  <div class="consent"><svg width="10" height="10"><rect x=".5" y="1.5" width="8" height="8" fill="none" stroke="#fff"/><path d="M2 5l2.5 3L10 1" stroke="#fff" stroke-width="1.4" fill="none"/></svg>Souhlasím s podmínkami použití</div>
  <div class="btn-small btn-blue">SPOCITAT CENU<span class="arr"><svg width="9" height="6"><path d="M0 3h8M5 0l3 3-3 3" stroke="#fff" fill="none"/></svg></span></div>
  <div class="brand">JISTOTKA.CZ</div>
</form>

<h2 class="abs h-section" style="left:0;width:837px;text-align:center;top:742px">UZAVŘELI JSTE V MINULOSTI NEVÝHODNOU POJISTKU? ZBAVTE SE JÍ!</h2>
<div class="abs rule" style="left:382px;top:768px"></div>

<div class="abs photo" role="img" aria-label="Ilustrace: dlaně tvoří střechu nad domkem nakresleným křídou pod deštivými mraky"></div>

<p class="abs para" style="left:405px;top:785px;width:333px">Máte pocit, že za stávající pojistku platíte zbytečně mnoho? Pojďte něco udělat. S námi najdete tu nejvýhodnější nabídku na trhu a na vše porovnáme. Je to nejsnazší cesta, jak se zbavit starého nevýhodného pojištění. Stačí kliknout a vydat se na cestu k levnější pojistce.</p>
<div class="abs btn-small btn-orange" style="left:405px;top:883px;width:84px;height:17px;line-height:17px;font-size:9.5px">CHCI USETRIT<span class="arr" style="width:17px;height:17px"><svg width="9" height="6"><path d="M0 3h8M5 0l3 3-3 3" stroke="#fff" fill="none"/></svg></span></div>
<h3 class="abs h-section" style="left:405px;top:921px;font-size:13px">JAK TO FUNGUJE</h3>
<div class="abs rule" style="left:405px;top:942px"></div>
<p class="abs para" style="left:405px;top:953px;width:333px">Lorem ipsum dolor sit amet, consectetuer adipiscing elit, sed diam nonummy nibh euismod tincidunt ut laoreet dolore magna aliquam erat volutpat. Ut wisi enim ad minim veniam, quis nostrud exerci tation ullamcorper suscipit lobortis nisl ut aliquip ex ea commodo consequat. Duis autem vel eum iriure dolor in hendrerit in vulputate.</p>

<section class="abs newsletter">
  <div class="label">ODEBIRAT NEWLETTER</div>
  <div class="input">E-mail</div>
  <div class="submit">POTVRDIT</div>
</section>

<footer class="abs footer">
  <div class="brand">JISTOTKA.CZ</div>
  <div class="social" style="left:381px" aria-label="Sociální síť"></div>
  <div class="social" style="left:409px" aria-label="Sociální síť"></div>
  <div class="social" style="left:436px" aria-label="Sociální síť"></div>
  <div class="legal">Ochrana soukromí | Podmínky použití<br>Copyright © 2017 Jistotka.cz. Všechna práva vyhrazena.</div>
</footer>
</body>
</html>
```